Dale Harwick Realtors
Stationary, Letterhead, Business Cards & Envelopes
Modern
Dale Harwick
Broker/ Owner
5817 Elmwood Crest Rd.
Fort Worth, Texas 76243
daleharwick@vesnamail.net
www.DaleHarwickRealtors.com
I would like the back to be the logo and I am not sure if it should have a white background or some color, I am open.
use logo here

```html
<!DOCTYPE html>
<html lang="en">
<head>
<meta charset="utf-8">
<title>Dale Harwick Realtors – Business Card</title>
<link href="https://fonts.googleapis.com/css2?family=Open+Sans:wght@400;600;700&display=swap" rel="stylesheet">
<style>
  :root {
    --backdrop: #e7e3dd;
    --card: #ffffff;
    --navy: #1c2b5c;
    --blue: #2c55a3;
    --sky: #8fb3df;
    --ink: #3a3f4a;
    --rule: #b9bfca;
  }
  * { box-sizing: border-box; margin: 0; padding: 0; }
  html, body { width: 1200px; height: 404px; overflow: hidden; }
  body {
    background: var(--backdrop);
    font-family: "Open Sans", Arial, sans-serif;
    position: relative;
  }
  .card {
    position: absolute;
    top: 41px;
    width: 500px;
    height: 331px;
    background: var(--card);
    border-radius: 14px;
    overflow: hidden;
    box-shadow: 0 2px 6px rgba(0,0,0,.18);
  }
  .card--front { left: 72px; }
  .card--back { left: 628px; }

  .brand { position: absolute; left: 0; right: 0; text-align: center; color: var(--navy); font-weight: 600; }
  .brand__mark { display: block; margin: 0 auto 10px; width: 44px; height: 44px; background: var(--navy); }
  .brand__name { display: block; font-size: 26px; letter-spacing: .5px; line-height: 1.1; }
  .card--front .brand { top: 30px; }
  .card--back .brand { top: 92px; }
  .card--back .brand__mark { width: 56px; height: 56px; margin-bottom: 16px; }
  .card--back .brand__name { font-size: 31px; }

  .address {
    position: absolute; left: 90px; top: 190px;
    font-style: normal; font-size: 11.5px; line-height: 17px; color: var(--ink);
  }
  .divider { position: absolute; left: 290px; top: 168px; width: 1px; height: 78px; background: var(--rule); }
  .contact { position: absolute; left: 305px; top: 166px; list-style: none; font-size: 11px; color: var(--ink); }
  .contact li { display: flex; align-items: center; height: 19.5px; white-space: nowrap; }
  .contact svg { width: 10px; height: 10px; margin-right: 8px; fill: var(--navy); flex: none; }

  .swoosh { position: absolute; left: 0; bottom: 0; width: 500px; height: 90px; }
  .signature {
    position: absolute; left: 24px; bottom: 18px;
    font-size: 13px; color: #fff;
  }
  .signature strong { font-weight: 700; }

  .web {
    position: absolute; left: 0; right: 0; top: 230px; text-align: center;
    font-size: 12.5px; letter-spacing: 1.6px; color: var(--ink);
  }
</style>
</head>
<body>
  <section class="card card--front" aria-label="Business card front">
    <div class="brand">
      <span class="brand__mark"></span>
      <span class="brand__name">Dale Harwick Realtors</span>
    </div>

    <address class="address">5817 Elmwood Crest Rd.<br>Fort Worth, Texas 76243</address>
    <div class="divider"></div>
    <ul class="contact">
      <li><svg viewBox="0 0 24 24"><path d="M6.6 10.8a15 15 0 006.6 6.6l2.2-2.2a1 1 0 011-.25 11.4 11.4 0 003.6.6 1 1 0 011 1V20a1 1 0 01-1 1A17 17 0 013 4a1 1 0 011-1h3.5a1 1 0 011 1c0 1.25.2 2.45.6 3.6a1 1 0 01-.25 1z"/></svg>817-402-5186</li>
      <li><svg viewBox="0 0 24 24"><path d="M6 3h10v5H6zM3 9h18v9h-3v3H6v-3H3zm5 6v4h8v-4z"/></svg>817-402-5187</li>
      <li><svg viewBox="0 0 24 24"><path d="M2 5h20v14H2zm2 2v.5l8 5 8-5V7z"/></svg>daleharwick@vesnamail.net</li>
      <li><svg viewBox="0 0 24 24"><circle cx="12" cy="12" r="10"/></svg>www.DaleHarwickRealtors.com</li>
    </ul>

    <svg class="swoosh" viewBox="0 0 500 90" preserveAspectRatio="none" aria-hidden="true">
      <path d="M0 30 C160 58 340 46 500 6 L500 90 L0 90 Z" fill="var(--sky)"/>
      <path d="M0 38 C165 66 340 56 500 18 L500 90 L0 90 Z" fill="var(--blue)"/>
      <path d="M0 44 C170 72 340 64 500 28 L500 90 L0 90 Z" fill="var(--navy)"/>
    </svg>
    <p class="signature"><strong>Dale Harwick</strong>, Broker/ Owner</p>
  </section>

  <section class="card card--back" aria-label="Business card back">
    <div class="brand">
      <span class="brand__mark"></span>
      <span class="brand__name">Dale Harwick Realtors</span>
    </div>
    <p class="web">www.DaleHarwickRealtors.com</p>
  </section>
</body>
</html>
```